a residential painting contractor I need a 6x9 postcard made

I already have a logo, I'm trying to offer my services to people. you can put that there's a 250$ discount for first time customers. include my License number #4627381 as well as the services I offer, interior and exterior painting, pressure washing, cabinet painting, epoxy floors, wood staining, decks, fences and much more. I'm licensed bonded and insured as well.

Target Market(s)

residential consumers (homeowners)

Industry/Entity Type

Painting contractor

Requirements
Must have
• postage stuff on the back I've linked some pictures top right please, my license number, what I do, phone number (555)317-0846 email velbrushworks7@mailzo.net, front and back of postcard
Nice to have
• well lit house in the background, maybe little circles of people doing some of the services I offer

```html
<!DOCTYPE html>
<html lang="en">
<head>
<meta charset="utf-8">
<title>Vel Brushworks – Postcard</title>
<link rel="stylesheet" href="https://fonts.googleapis.com/css2?family=Cinzel:wght@400;700&family=Roboto:wght@400;700&family=Roboto+Condensed:wght@700&display=swap">
<style>
  :root {
    --brand-blue: #1c449c;
    --brand-red: #e8334a;
    --ink: #1d1d1f;
    --paper: #ffffff;
    --panel-grey: #e9e9eb;
    --backdrop: #e7e2dc;
  }
  * { margin: 0; padding: 0; box-sizing: border-box; }
  html, body { width: 960px; height: 1200px; overflow: hidden; }
  body { background: var(--backdrop); position: relative; font-family: "Roboto", Arial, sans-serif; color: var(--ink); }

  .card { position: absolute; left: 75px; width: 810px; height: 540px; background: var(--paper); overflow: hidden; box-shadow: 0 4px 14px rgba(0,0,0,.18); }
  .card--front { top: 40px; }
  .card--back { top: 614px; }
  .abs { position: absolute; }

  /* brand mark */
  .brand { display: flex; flex-direction: column; align-items: center; justify-content: center; gap: 10px; }
  .brand__dot { width: 64px; height: 64px; border-radius: 50%; background: var(--ink); }
  .brand__name { font-family: "Cinzel", Georgia, serif; font-weight: 700; color: var(--ink); white-space: nowrap; }
  .card--front .brand { left: 26px; top: 22px; width: 150px; height: 134px; }
  .card--front .brand__name { font-size: 14px; }
  .card--back .brand { left: 8px; top: 24px; width: 140px; height: 120px; gap: 9px; }
  .card--back .brand__dot { width: 56px; height: 56px; }
  .card--back .brand__name { font-size: 12.5px; }

  .headline { font-family: "Cinzel", Georgia, serif; font-weight: 400; color: var(--ink); text-transform: uppercase; }
  .card--front .headline { left: 189px; top: 30px; font-size: 36px; line-height: 36px; }
  .card--back .headline { left: 163px; top: 34px; font-size: 32px; line-height: 33px; }

  /* front */
  .hero-photo { left: 350px; top: 0; width: 460px; height: 350px;
    background: linear-gradient(90deg, rgba(255,255,255,0) 0%, #e4e7ee 22%, #8d9ab3 48%, #2c3b5c 66%, #1f2b46 100%); }
  .services-tag { left: 33px; top: 174px; width: 220px; height: 31px; background: var(--ink); color: #fff;
    font-weight: 700; font-size: 18px; line-height: 31px; padding-left: 8px; transform: rotate(-.6deg); }
  .services-list { left: 48px; top: 212px; list-style: none; font-size: 14.5px; }
  .services-list li { display: flex; align-items: center; height: 23.8px; }
  .services-list svg { width: 13px; height: 13px; margin-right: 7px; flex: none; }
  .seal { position: absolute; }
  .card--front .seal { left: 439px; top: 186px; width: 170px; height: 136px; }
  .card--back .seal { left: 350px; top: 30px; width: 136px; height: 109px; }

  .offer-band { left: 81px; top: 348px; width: 729px; height: 113px; background: var(--brand-blue); }
  .roller-art { left: 0; top: 350px; width: 120px; height: 110px;
    background: linear-gradient(90deg, rgba(28,68,156,0) 0%, rgba(28,68,156,.15) 60%, #3f5ab8 68%, #2a47a6 100%); }
  .offer { color: #fff; font-family: "Cinzel", Georgia, serif; }
  .offer__label { font-weight: 700; letter-spacing: 1px; }
  .offer__amount { font-weight: 700; white-space: nowrap; }
  .offer__note { font-weight: 400; letter-spacing: 1.2px; white-space: nowrap; }
  .card--front .offer { left: 147px; top: 362px; }
  .card--front .offer__label { font-size: 17px; line-height: 20px; }
  .card--front .offer__amount { font-size: 46px; line-height: 48px; }
  .card--front .offer__note { font-size: 12.5px; line-height: 18px; }
  .band-rule { left: 398px; top: 363px; width: 1px; height: 87px; background: rgba(255,255,255,.6); }
  .phone-ring { border-radius: 50%; display: flex; align-items: center; justify-content: center; }
  .card--front .phone-ring { left: 438px; top: 376px; width: 58px; height: 58px; border: 2.5px solid #fff; }
  .card--front .phone-ring svg { width: 34px; height: 34px; fill: #fff; }
  .cta { white-space: nowrap; }
  .cta__lead b { font-weight: 700; }
  .cta__number { font-weight: 700; }
  .card--front .cta { left: 506px; top: 372px; color: #fff; }
  .card--front .cta__lead { font-size: 17.5px; line-height: 22px; }
  .card--front .cta__number { font-size: 36px; line-height: 40px; }

  .creds-shield { left: 36px; top: 480px; width: 32px; height: 40px; }
  .creds { font-family: "Roboto Condensed", Arial, sans-serif; font-weight: 700; text-transform: uppercase; color: var(--ink); }
  .card--front .creds { left: 78px; top: 481px; font-size: 16.5px; line-height: 19px; }
  .foot-rule { left: 261px; top: 476px; width: 1px; height: 50px; background: #cfcfcf; }
  .license { left: 284px; top: 480px; }
  .license__label { font-size: 14px; line-height: 18px; }
  .license__number { font-size: 19px; line-height: 24px; font-weight: 700; }
  .mail-dot { border-radius: 50%; display: flex; align-items: center; justify-content: center; }
  .card--front .mail-dot { left: 513px; top: 484px; width: 34px; height: 34px; background: var(--brand-red); }
  .card--front .mail-dot svg { width: 18px; height: 18px; fill: #fff; }
  .email { white-space: nowrap; }
  .card--front .email { left: 555px; top: 491px; font-size: 16.5px; }

  /* back */
  .back-panel { left: 0; top: 0; width: 432px; height: 540px; background: var(--panel-grey);
    clip-path: polygon(0 0, 416px 0, 420px 40px, 414px 120px, 424px 220px, 418px 300px, 426px 380px, 410px 450px, 298px 460px, 296px 540px, 0 540px); }
  .postage { left: 661px; top: 28px; width: 120px; height: 89px; border: 1px solid #555; text-align: center;
    font-weight: 700; font-size: 12.5px; line-height: 16.5px; padding-top: 2px; color: #111; }
  .postage__paid { font-size: 16px; line-height: 19px; }
  .gallery { left: 14px; top: 163px; width: 396px; height: 107px; background: #fff; display: flex; gap: 3px; padding: 2px; }
  .gallery__tile { flex: 1; }
  .tile--exterior { background: linear-gradient(160deg, #9ccbe3 0%, #8fb9b8 45%, #c9d3cf 100%); }
  .tile--interior { background: linear-gradient(170deg, #e6e4df 0%, #ddd8cf 55%, #c99a62 100%); }
  .tile--deck { background: linear-gradient(100deg, #6e4530 0%, #a0684a 45%, #7a4a33 100%); }
  .offer-box { left: 0; top: 292px; width: 274px; height: 109px; background: var(--brand-blue); }
  .card--back .offer { left: 28px; top: 304px; }
  .card--back .offer__label { font-size: 18px; line-height: 22px; }
  .card--back .offer__amount { font-size: 41px; line-height: 44px; }
  .card--back .offer__note { font-size: 13px; line-height: 16px; }
  .card--back .creds { left: 303px; top: 298px; font-size: 16.5px; line-height: 19px; }
  .roller-photo { left: 297px; top: 368px; width: 150px; height: 172px;
    background: linear-gradient(180deg, #d9d9d9 0%, #bdbdbd 28%, #ececec 34%, #f4f4f4 86%, #3a5fc0 92%, #2b4fae 100%); }
  .card--back .phone-ring { left: 24px; top: 429px; width: 42px; height: 42px; border: 2px solid var(--ink); }
  .card--back .phone-ring svg { width: 25px; height: 25px; fill: var(--ink); }
  .card--back .cta { left: 75px; top: 426px; color: var(--ink); }
  .card--back .cta__lead { font-size: 14px; line-height: 18px; }
  .card--back .cta__number { font-size: 27px; line-height: 32px; }
  .card--back .mail-dot { left: 31px; top: 489px; width: 28px; height: 28px; border: 1.5px solid var(--ink); }
  .card--back .mail-dot svg { width: 14px; height: 14px; fill: var(--ink); }
  .card--back .email { left: 75px; top: 493px; font-size: 16px; }
</style>
</head>
<body>

<svg width="0" height="0" style="position:absolute">
  <defs>
    <symbol id="icon-phone" viewBox="0 0 24 24"><path d="M6.6 10.8c1.4 2.8 3.8 5.1 6.6 6.6l2.2-2.2c.3-.3.7-.4 1-.2 1.1.4 2.3.6 3.6.6.6 0 1 .4 1 1V20c0 .6-.4 1-1 1C10.6 21 3 13.4 3 4c0-.6.4-1 1-1h3.5c.6 0 1 .4 1 1 0 1.3.2 2.5.6 3.6.1.3 0 .7-.2 1L6.6 10.8z"/></symbol>
    <symbol id="icon-mail" viewBox="0 0 24 24"><path d="M3 5h18v14H3z M4.5 6.5v.4L12 12l7.5-5.1v-.4z" fill-rule="evenodd"/></symbol>
    <symbol id="plain-seal" viewBox="0 0 170 136">
      <circle cx="85" cy="68" r="64" fill="#1d1d1f" stroke="#fff" stroke-width="3"/>
    </symbol>
  </defs>
</svg>

<!-- Front of postcard -->
<section class="card card--front">
  <div class="abs hero-photo" role="img" aria-label="Photo of a painter in a navy work shirt holding a paint roller"></div>

  <div class="abs brand">
    <span class="brand__dot"></span>
    <span class="brand__name">VEL BRUSHWORKS</span>
  </div>
  <h1 class="abs headline">Expert<br>Painting<br>Service</h1>

  <div class="abs services-tag">SERVICES OFFERED</div>
  <ul class="abs services-list">
    <li><svg viewBox="0 0 14 14"><path d="M1 7.5l4 4L13 2.5" fill="none" stroke="#e8334a" stroke-width="2.4"/></svg>Interior and exterior painting</li>
    <li><svg viewBox="0 0 14 14"><path d="M1 7.5l4 4L13 2.5" fill="none" stroke="#e8334a" stroke-width="2.4"/></svg>Pressure washing</li>
    <li><svg viewBox="0 0 14 14"><path d="M1 7.5l4 4L13 2.5" fill="none" stroke="#e8334a" stroke-width="2.4"/></svg>Cabinet painting</li>
    <li><svg viewBox="0 0 14 14"><path d="M1 7.5l4 4L13 2.5" fill="none" stroke="#e8334a" stroke-width="2.4"/></svg>Epoxy floors</li>
    <li><svg viewBox="0 0 14 14"><path d="M1 7.5l4 4L13 2.5" fill="none" stroke="#e8334a" stroke-width="2.4"/></svg>Wood staining, decks, fences and much more.</li>
  </ul>

  <svg class="seal" role="img" aria-label="Quality guarantee seal"><use href="#plain-seal"/></svg>

  <div class="abs offer-band"></div>
  <div class="abs roller-art" role="img" aria-label="Blue paint roller rolling out the offer band"></div>
  <div class="abs offer">
    <div class="offer__label">DISCOUNT</div>
    <div class="offer__amount">250$ OFF</div>
    <div class="offer__note">FOR FIRST TIME CUSTOMERS</div>
  </div>
  <div class="abs band-rule"></div>
  <div class="abs phone-ring"><svg><use href="#icon-phone"/></svg></div>
  <div class="abs cta">
    <div class="cta__lead">Call now for <b>FREE ESTIMATE</b></div>
    <div class="cta__number">(555)317-0846</div>
  </div>

  <svg class="abs creds-shield" viewBox="0 0 32 40"><path d="M16 1L31 6v13c0 10-7 16-15 20C8 35 1 29 1 19V6z" fill="#e8334a"/><path d="M8.5 20l5 5 10-11" fill="none" stroke="#fff" stroke-width="3"/></svg>
  <div class="abs creds">Specialist, licensed<br>and insured</div>
  <div class="abs foot-rule"></div>
  <div class="abs license">
    <div class="license__label">License number</div>
    <div class="license__number">#4627381</div>
  </div>
  <div class="abs mail-dot"><svg><use href="#icon-mail"/></svg></div>
  <div class="abs email">velbrushworks7@mailzo.net</div>
</section>

<!-- Back of postcard -->
<section class="card card--back">
  <div class="abs back-panel"></div>

  <div class="abs brand">
    <span class="brand__dot"></span>
    <span class="brand__name">VEL BRUSHWORKS</span>
  </div>
  <h2 class="abs headline">Expert<br>Painting<br>Service</h2>
  <svg class="seal" role="img" aria-label="Quality guarantee seal"><use href="#plain-seal"/></svg>

  <div class="abs postage">
    PRSRT STD<br>ECRWSS<br>U.S.POSTAGE<br><span class="postage__paid">PAID</span><br>EDDM Retail
  </div>

  <div class="abs gallery">
    <div class="gallery__tile tile--exterior" role="img" aria-label="Freshly painted house exterior"></div>
    <div class="gallery__tile tile--interior" role="img" aria-label="Bright painted living room interior"></div>
    <div class="gallery__tile tile--deck" role="img" aria-label="Wooden deck being stained"></div>
  </div>

  <div class="abs offer-box"></div>
  <div class="abs offer">
    <div class="offer__label">DISCOUNT</div>
    <div class="offer__amount">250$ OFF</div>
    <div class="offer__note">FOR FIRST TIME CUSTOMERS</div>
  </div>

  <div class="abs creds">Specialist,<br>licensed<br>and insured</div>
  <div class="abs roller-photo" role="img" aria-label="Paint roller with blue handle"></div>

  <div class="abs phone-ring"><svg><use href="#icon-phone"/></svg></div>
  <div class="abs cta">
    <div class="cta__lead">Call now for <b>FREE ESTIMATE</b></div>
    <div class="cta__number">(555)317-0846</div>
  </div>
  <div class="abs mail-dot"><svg><use href="#icon-mail"/></svg></div>
  <div class="abs email">velbrushworks7@mailzo.net</div>
</section>

</body>
</html>
```